Business Card + Stationery Design for a Craft Beer Bar

Mr. Tovell's is a taproom sport bar that contains in its menu beers from different places around the world. What we offer differently is the experience that you can get inside our location, ambient music with rock from the 80s to 90s, projection with the sports of the moment, board games and private events.

Target Market(s)

Young people, Mid and High Class

Industry/Entity Type

Business

Font styles to use
Serif
Sans Serif

Colors
fee18a

Requirements
Must have
• Name, Title, Contact Details, Website
Nice to have
• Mail Signature
Should not have
• n/a

```html
<!DOCTYPE html>
<html lang="en">
<head>
<meta charset="utf-8">
<title>Mr. Tovell's Taproom – Business Card</title>
<link rel="stylesheet" href="https://fonts.googleapis.com/css2?family=Oswald:wght@600&family=Montserrat:wght@400;500&display=swap">
<style>
  :root {
    --backdrop: #3b322d;
    --card: #1c1c1c;
    --card-edge: #121212;
    --white: #f4f2ee;
    --gold: #fee18a;
    --gold-deep: #e8b84c;
    --muted: #8c8780;
  }
  * { margin: 0; padding: 0; box-sizing: border-box; }
  html, body { width: 1200px; height: 715px; overflow: hidden; }
  body {
    background: var(--backdrop);
    display: flex;
    align-items: center;
    justify-content: center;
    gap: 100px;
  }
  .card {
    width: 320px;
    height: 560px;
    background: var(--card);
    border: 1px solid var(--card-edge);
    border-radius: 6px;
    box-shadow: 0 12px 30px rgba(0,0,0,0.45);
    position: relative;
    display: flex;
    flex-direction: column;
    align-items: center;
    color: var(--white);
  }
  .card--front { justify-content: center; }
  .card--back { padding-top: 90px; }

  .brand { text-align: center; }
  .brand__est {
    font-family: "Montserrat", sans-serif;
    font-size: 9px;
    letter-spacing: 2px;
    color: var(--muted);
    margin-bottom: 14px;
  }
  .brand__name {
    font-family: "Oswald", sans-serif;
    font-weight: 600;
    font-size: 38px;
    line-height: 1.05;
    letter-spacing: 1px;
    text-transform: uppercase;
    color: var(--white);
  }

  .contact {
    margin-top: 70px;
    width: 240px;
    align-self: flex-start;
    margin-left: 42px;
  }
  .contact__person {
    font-family: "Oswald", sans-serif;
    font-weight: 600;
    font-size: 30px;
    letter-spacing: 1px;
    color: var(--gold-deep);
    text-transform: uppercase;
  }
  .contact__rule {
    width: 46px;
    height: 2px;
    background: var(--gold-deep);
    margin: 14px 0;
  }
  .contact__list {
    list-style: none;
    font-family: "Montserrat", sans-serif;
    font-size: 11px;
    letter-spacing: 2px;
    line-height: 1.9;
    text-transform: uppercase;
  }
  .contact__label { color: var(--gold-deep); }
  .contact__value { color: var(--white); }
  .contact__address {
    font-family: "Montserrat", sans-serif;
    font-size: 11px;
    letter-spacing: 2px;
    line-height: 1.9;
    text-transform: uppercase;
    font-style: normal;
    color: var(--white);
  }
</style>
</head>
<body>
  <section class="card card--front" aria-label="Business card front">
    <div class="brand">
      <p class="brand__est">EST. 2017</p>
      <p class="brand__name">Mr. Tovell's<br>Taproom</p>
    </div>
  </section>

  <section class="card card--back" aria-label="Business card back">
    <div class="brand">
      <p class="brand__est">EST. 2017</p>
      <p class="brand__name">Mr. Tovell's<br>Taproom</p>
    </div>
    <div class="contact">
      <p class="contact__person">Mr. Tovell</p>
      <div class="contact__rule"></div>
      <ul class="contact__list">
        <li><span class="contact__label">Phone: </span><span class="contact__value">(123) 555-0148</span></li>
        <li><span class="contact__label">Email: </span><span class="contact__value">info@mrtovells.com</span></li>
        <li><span class="contact__label">Web: </span><span class="contact__value">www.mrtovells.com</span></li>
      </ul>
      <div class="contact__rule"></div>
      <address class="contact__address">418 Linden Avenue<br>Fairview, AL 35099</address>
    </div>
  </section>
</body>
</html>
```